I am a Korrabel Service and Marketing Consultant looking for a Korrabelesque but business like cover wit

I need a bookcover designed for my new business book titled; "Steady Sparkle. 9 Golden Rules To Korrabelify Your Firm. Win Loyal Clients & Grow Lasting Profits Through EVERY Season"

The name of my company is Brightwell Guest Works

We work with companies to implement Korrabel Style Service and Themeing, and then create marketing campaigns to promote that level of service.

I have used Mouse Memory font in the past, but am not tied to it

Small Business owners, medical practices, law firms

Business

• Colors: RGB 30, 54, 128 AND 113, 191, 76. These are the two colors in my logo, if you need it.
• Magic Key?? Gloved Hand (similar to a Korrabel Character)??
• Any copyright protected inages

```html
<!DOCTYPE html>
<html lang="en">
<head>
<meta charset="UTF-8">
<title>Steady Sparkle – Book Cover Wrap</title>
<link rel="stylesheet" href="https://fonts.googleapis.com/css2?family=Marcellus&family=Crimson+Text:wght@400;600&display=swap">
<style>
  :root {
    --page-bg: #d9d9d9;
    --cover-bg: #141414;
    --spine-bg: #1b1b1b;
    --ink-light: #e4e4e4;
    --ink-soft: #bdbdbd;
    --panel-white: #f2f2f2;
    --brand-navy: rgb(30, 54, 128);
    --photo-dark: #1a1a1a;
    --photo-mid: #6e6e6e;
  }
  * { margin: 0; padding: 0; box-sizing: border-box; }
  html, body { width: 1200px; height: 800px; overflow: hidden; }
  body {
    background: var(--page-bg);
    font-family: "Crimson Text", Georgia, serif;
    position: relative;
  }
  .cover-wrap {
    position: absolute;
    left: 175px;
    top: 70px;
    width: 850px;
    height: 660px;
    display: flex;
  }
  .back-cover, .front-cover {
    width: 400px;
    height: 100%;
    background: var(--cover-bg);
    position: relative;
    color: var(--ink-light);
  }
  .spine {
    width: 50px;
    height: 100%;
    background: var(--spine-bg);
    color: var(--ink-light);
    display: flex;
    flex-direction: column;
    align-items: center;
    padding-top: 22px;
  }
  .spine-title {
    writing-mode: vertical-rl;
    font-family: "Marcellus", Georgia, serif;
    font-size: 24px;
    letter-spacing: 5px;
  }
  .spine-author {
    writing-mode: vertical-rl;
    font-size: 13px;
    margin-top: 34px;
    color: var(--ink-soft);
  }
  .author-top {
    position: absolute;
    top: 20px;
    right: 36px;
    font-size: 14px;
  }
  .book-title {
    font-family: "Marcellus", Georgia, serif;
    font-weight: 400;
    text-align: center;
    letter-spacing: 1px;
  }
  .back-cover .book-title { margin-top: 46px; font-size: 32px; }
  .book-subtitle {
    font-family: "Marcellus", Georgia, serif;
    font-weight: 400;
    text-align: center;
    letter-spacing: 0.3px;
  }
  .back-cover .book-subtitle { font-size: 13.5px; margin-top: 4px; }
  .back-blurb {
    margin: 14px 30px 0;
    font-size: 11.6px;
    line-height: 1.22;
    text-align: justify;
    text-align-last: center;
    color: var(--ink-soft);
  }
  .back-footer {
    position: absolute;
    left: 30px;
    right: 30px;
    bottom: 34px;
    display: flex;
    justify-content: space-between;
  }
  .publisher-box, .isbn-box {
    background: var(--panel-white);
    height: 56px;
    display: flex;
    align-items: center;
    justify-content: center;
    gap: 6px;
  }
  .publisher-box { width: 156px; }
  .isbn-box { width: 128px; font-size: 16px; color: #333; }
  .publisher-name {
    font-size: 11.5px;
    color: var(--brand-navy);
    font-weight: 400;
  }
  .publisher-dot {
    width: 10px; height: 10px; border-radius: 50%;
    background: var(--brand-navy);
    flex-shrink: 0;
  }
  .front-cover .book-title { margin-top: 52px; font-size: 38px; }
  .front-cover .book-subtitle { font-size: 15px; margin-top: 6px; }
  .cover-photo {
    width: 300px;
    height: 300px;
    margin: 40px auto 0;
    background: radial-gradient(ellipse at 55% 50%, var(--photo-mid) 0%, #3a3a3a 45%, var(--photo-dark) 75%);
  }
  .tagline {
    margin-top: 34px;
    text-align: center;
    font-size: 17px;
    line-height: 1.25;
  }
  .author-front {
    text-align: center;
    font-size: 17px;
    margin-top: 26px;
  }
</style>
</head>
<body>
  <div class="cover-wrap">
    <section class="back-cover">
      <p class="author-top">Author Name</p>
      <h2 class="book-title">STEADY SPARKLE</h2>
      <p class="book-subtitle">9 GOLDEN RULES TO KORRABELIFY YOUR FIRM</p>
      <p class="back-blurb">Every business has a chance to make people feel something special. In this practical guide, you will learn how leading service brands turn ordinary visits into moments that guests remember and share. Each of the nine golden rules is built on years of hands-on work with small firms, medical practices and law offices that wanted more than satisfied clients. They wanted loyal fans. You will discover how to design a welcome that sets the tone, train a team that acts with care, and shape every small detail so it supports the story you want to tell. You will see how thoughtful service lets you charge fair prices with confidence, and how a clear promise makes your marketing easier and more honest. Simple checklists and real examples help you put each idea to work the same week you read it. Whether the market is rising or falling, these rules give you a steady way to stand out, keep clients coming back and grow profits that last. Start today, and let your firm become the place people talk about for all the right reasons.</p>
      <div class="back-footer">
        <div class="publisher-box">
          <span class="publisher-dot"></span>
          <span class="publisher-name">Brightwell Guest Works</span>
        </div>
        <div class="isbn-box">ISBN</div>
      </div>
    </section>

    <section class="spine">
      <span class="spine-title">STEADY SPARKLE</span>
      <span class="spine-author">Author Name</span>
    </section>

    <section class="front-cover">
      <h1 class="book-title">STEADY SPARKLE</h1>
      <p class="book-subtitle">9 GOLDEN RULES TO KORRABELIFY YOUR FIRM</p>
      <div class="cover-photo" role="img" aria-label="Black and white photograph of a magician's hands in a suit tucking a playing card with a red heart into the sleeve"></div>
      <p class="tagline">Win Loyal Clients &amp; Grow Lasting Profits<br>Through EVERY Season</p>
      <p class="author-front">Author Name</p>
    </section>
  </div>
</body>
</html>
```